Commercial Construction Company

We need a business card design based on our current logo. We are a commercial general contractor based in Southern California that specializes in bank remodels. We would like to see designs that incorporate dark blue. The final design should portray an image of professionalism and quality.

If possible, I would like to add metallic foil to the design. Thank you

```html
<!DOCTYPE html>
<html lang="en">
<head>
<meta charset="utf-8">
<title>Kestrel Commercial Builders Business Card</title>
<link href="https://fonts.googleapis.com/css2?family=Montserrat:wght@400;500;600;700&display=swap" rel="stylesheet">
<style>
  :root {
    --stage: #2a2c30;
    --navy: #0f4a8a;
    --white: #ffffff;
    --ink: #1c1c1c;
    --grey: #9a9a9a;
  }
  * { box-sizing: border-box; margin: 0; padding: 0; }
  html, body { width: 1200px; height: 900px; overflow: hidden; }
  body {
    background: var(--stage);
    font-family: "Montserrat", Arial, sans-serif;
    position: relative;
  }
  .card {
    position: absolute;
    top: 307px;
    width: 500px;
    height: 286px;
    border-radius: 26px;
    overflow: hidden;
  }
  .card--front { left: 70px; background: var(--white); }
  .card--back { left: 630px; background: var(--navy); }

  .brand {
    position: absolute;
    display: flex;
    align-items: center;
    gap: 10px;
    font-weight: 700;
    letter-spacing: 2px;
    white-space: nowrap;
  }
  .brand__dot { border-radius: 50%; flex: none; }
  .card--front .brand { left: 40px; top: 42px; font-size: 28px; color: var(--navy); }
  .card--front .brand__dot { width: 22px; height: 22px; background: var(--navy); }
  .card--back .brand {
    left: 50%; top: 50%; transform: translate(-50%, -50%);
    font-size: 44px; color: var(--white);
  }
  .card--back .brand__dot { width: 32px; height: 32px; background: var(--white); }

  .person { position: absolute; left: 200px; top: 112px; }
  .person__name { font-size: 27px; font-weight: 700; letter-spacing: 1px; line-height: 1; white-space: nowrap; }
  .person__first { color: var(--navy); }
  .person__last { color: var(--grey); font-weight: 500; }
  .person__title { font-size: 13px; color: var(--ink); margin-top: 4px; }

  .contacts { position: absolute; left: 178px; top: 178px; list-style: none; }
  .contacts li {
    display: flex; align-items: center; gap: 10px;
    font-size: 13px; color: var(--ink); margin-bottom: 12px;
    white-space: nowrap;
  }
  .contacts svg { width: 14px; height: 14px; flex: none; }
</style>
</head>
<body>
  <section class="card card--front">
    <div class="brand"><span class="brand__dot"></span>KESTREL</div>
    <div class="person">
      <p class="person__name"><span class="person__first">MARLO</span> <span class="person__last">TENNANT</span></p>
      <p class="person__title">President &amp; CEO</p>
    </div>
    <ul class="contacts">
      <li>
        <svg viewBox="0 0 14 14" fill="none" stroke="#0f4a8a" stroke-width="1.3"><rect x="3.5" y="1" width="7" height="12" rx="1.5"/></svg>
        555-014-2280
      </li>
      <li>
        <svg viewBox="0 0 14 14" fill="none" stroke="#0f4a8a" stroke-width="1.3"><rect x="1" y="3" width="12" height="8.5" rx="1"/><path d="M1 3.5 7 8l6-4.5"/></svg>
        kestrelcommercialbuild@mail.com
      </li>
      <li>
        <svg viewBox="0 0 14 14" fill="none" stroke="#0f4a8a" stroke-width="1.3"><path d="M1.5 7 7 2l5.5 5M3 6v6h8V6"/></svg>
        kestrelbuilders.com
      </li>
    </ul>
  </section>

  <section class="card card--back">
    <div class="brand"><span class="brand__dot"></span>KESTREL</div>
  </section>
</body>
</html>
```